Legal Information Website

We need a website that will serve as a source of information for people visiting, living, and working in the United Arab Emirates, where they can go and read about legal issues, laws, crimes, and most important find legal advice and find lawyers. The following are the pages of the website:

Find a Lawyer (Home Page)
This main feature of this page should be "Find a Lawyer"
Find a Lawyer should include the searching option by practice, by lawyer’s name, by law firm name or by location.

Ask a lawyer
This function allows the user to ask a lawyer a legal question and get an answer directly from a lawyer.

Research a legal matter
This function allows the user to do research on a certain legal topic. He/she can select from different legal topics.

Contact Us:
This page should include our contact details for the visitors in case they need any assistance. Contact us by Phone, Email, or Chat.

Once the design is approved, we will provide the rest of the website text.

Target Market(s)

General Public who seek legal advice

Industry/Entity Type

Law Firm

Font styles to use
Serif
Sans Serif

Requirements
Must have
• A tool to search for lawyer's, and then display the lawyer's picture and profile and credentials.

```html
<!DOCTYPE html>
<html lang="en">
<head>
<meta charset="utf-8">
<title>Cedra Group – Find a Lawyer</title>
<link href="https://fonts.googleapis.com/css2?family=Arimo:wght@400;700&family=Carlito:wght@400;700&display=swap" rel="stylesheet">
<style>
:root{
  --red:#b3261e;
  --red-dark:#8f1c16;
  --ink:#1f1f1f;
  --text:#333;
  --muted:#666;
  --line:#e3e3e3;
  --header-bg:#f7f7f7;
  --nav-top:#3f2d2b;
  --nav-bottom:#1c1111;
  --search-bg:#2b2b2b;
  --footer-bg:#2f2f2f;
  --white:#fff;
}
*{box-sizing:border-box;margin:0;padding:0}
html,body{width:846px;height:1200px;overflow:hidden}
body{position:relative;background:var(--white);font-family:"Arimo",Arial,sans-serif;color:var(--text)}
.abs{position:absolute}

/* header */
.site-header{position:absolute;left:0;top:0;width:846px;height:86px;background:var(--header-bg)}
.brand{position:absolute;left:72px;top:30px;display:flex;align-items:center;gap:7px;font-family:"Carlito",sans-serif;font-size:22px;font-weight:700;color:var(--ink);letter-spacing:1px}
.brand-mark{width:10px;height:10px;background:var(--red)}
.phone{position:absolute;left:543px;top:33px;display:flex;align-items:center;gap:9px;font-size:11px;color:var(--ink)}
.phone-icon{width:25px;height:25px;border-radius:50%;background:#6b6b6b;display:flex;align-items:center;justify-content:center}
.live-chat{position:absolute;left:680px;top:32px;width:96px;height:27px;background:var(--red);border-radius:3px;color:var(--white);font-size:12px;display:flex;align-items:center;justify-content:center;gap:9px}

/* navigation */
.main-nav{position:absolute;left:0;top:86px;width:846px;height:36px;background:linear-gradient(var(--nav-top),var(--nav-bottom))}
.main-nav a{position:absolute;top:0;height:36px;line-height:36px;color:var(--white);font-size:10px;text-decoration:none}
.main-nav a.active{background:var(--red);width:81px;left:71px;text-align:center}

/* hero */
.hero-photo{left:71px;top:141px;width:705px;height:272px;background:linear-gradient(180deg,#a7bccd 0%,#cfbfa4 30%,#b9a485 60%,#6e6155 100%)}
.slide-arrow{top:269px;width:28px;height:28px;border-radius:50%;background:rgba(0,0,0,.35);display:flex;align-items:center;justify-content:center}
.slide-arrow span{width:20px;height:20px;border-radius:50%;background:#f2f2f2;display:flex;align-items:center;justify-content:center}
.search-bar{left:71px;top:413px;width:705px;height:63px;background:var(--search-bg)}
.search-shadow{left:200px;top:476px;width:450px;height:14px;background:radial-gradient(ellipse at top,rgba(0,0,0,.18),transparent 70%)}
.select{position:absolute;top:17px;width:134px;height:29px;background:var(--white);border-radius:2px;font-size:7.5px;color:#444;padding-left:15px;line-height:29px}
.select::after{content:"";position:absolute;right:11px;top:12px;border-left:4px solid transparent;border-right:4px solid transparent;border-top:6px solid #333}
.search-btn{position:absolute;left:615px;top:17px;width:77px;height:29px;background:var(--red);color:var(--white);font-size:13px;text-align:center;line-height:29px}

/* feature cards */
.card{position:absolute;top:506px;width:225px;height:273px;border:1px solid var(--line);background:var(--white)}
.card-photo{height:128px;margin:1px}
.card h3{font-family:"Carlito",sans-serif;font-weight:400;font-size:14px;color:var(--ink);margin:18px 0 0 13px;letter-spacing:.3px}
.card p{font-size:8px;line-height:15.5px;margin:12px 13px 0 13px;color:var(--text);text-align:justify}
.btn{display:inline-block;background:var(--red);color:var(--white);font-size:9.5px;padding:0 9px;height:23px;line-height:23px}
.card .btn{position:absolute;left:14px;top:230px}

/* section headings */
.section-title{font-family:"Carlito",sans-serif;font-size:16px;font-weight:400;color:var(--ink);top:803px}
.rule{top:830px;height:1px;background:var(--line)}
.rule::before{content:"";position:absolute;left:0;top:0;width:60px;height:1px;background:var(--red)}
.pager{top:806px;font-size:11px;color:#666;letter-spacing:10px}

/* news */
.news-photo{left:71px;width:107px;height:82px}
.news-title{left:200px;font-family:"Carlito",sans-serif;font-size:12.5px;color:var(--ink)}
.news-date{left:200px;font-family:"Carlito",sans-serif;font-size:12px;color:var(--ink)}
.news-text{left:200px;width:237px;font-size:7.8px;line-height:15.5px;text-align:justify;color:var(--text)}
.read-more{color:var(--red);float:right}
.divider{left:71px;width:366px;height:1px;background:var(--line)}

/* blog */
.blog-card{left:466px;top:849px;width:312px;height:236px;border:1px solid var(--line)}
.blog-photo{height:113px;background:linear-gradient(120deg,#e9e6df 0%,#d9d3c8 45%,#a86a1e 60%,#6b3d10 80%,#d8d2c6 100%)}
.blog-card h3{font-family:"Carlito",sans-serif;font-weight:400;font-size:12.5px;color:var(--ink);padding:10px 0 0 13px;height:33px}
.blog-card hr{border:0;border-top:1px solid var(--line)}
.blog-meta{font-family:"Carlito",sans-serif;font-size:7.5px;color:#444;padding:10px 13px 0}
.blog-card p{font-size:8px;line-height:15.5px;color:var(--text);padding:9px 13px 0;text-align:justify}

/* footer */
.site-footer{position:absolute;left:0;top:1115px;width:846px;height:85px;background:var(--footer-bg);color:var(--white)}
.footer-links{position:absolute;left:71px;top:23px;font-size:8px}
.copyright{position:absolute;left:71px;top:50px;font-size:8px}
.social{position:absolute;top:30px;width:22px;height:22px;border-radius:50%;background:#e5e5e5}
</style>
</head>
<body>

<header class="site-header">
  <div class="brand"><span class="brand-mark"></span>CEDRA GROUP</div>
  <div class="phone">
    <span class="phone-icon">
      <svg width="12" height="10" viewBox="0 0 12 10"><path d="M1 3 Q6 -1 11 3 L10 5 L8 4 L8 3 Q6 2 4 3 L4 4 L2 5 Z M3 5 H9 L10 9 H2 Z" fill="#fff"/></svg>
    </span>
    +1(555) 014-2290
  </div>
  <div class="live-chat">
    <svg width="11" height="13" viewBox="0 0 11 13"><circle cx="5.5" cy="3.5" r="3" fill="#fff"/><path d="M0 13 Q0 7 5.5 7 Q11 7 11 13 Z" fill="#fff"/></svg>
    Live Chat
  </div>
</header>

<nav class="main-nav">
  <a class="active" href="#">Home</a>
  <a href="#" style="left:175px">Find a Lawyer</a>
  <a href="#" style="left:292px">Know your rights</a>
  <a href="#" style="left:423px">News</a>
  <a href="#" style="left:502px">Articles</a>
  <a href="#" style="left:590px">Contact us</a>
</nav>

<div class="abs hero-photo" role="img" aria-label="Crowd of people in traditional dress entering a federal court building"></div>
<div class="abs slide-arrow" style="left:85px"><span><svg width="6" height="9" viewBox="0 0 6 9"><path d="M5 1 L1 4.5 L5 8" stroke="#555" stroke-width="1.5" fill="none"/></svg></span></div>
<div class="abs slide-arrow" style="left:734px"><span><svg width="6" height="9" viewBox="0 0 6 9"><path d="M1 1 L5 4.5 L1 8" stroke="#555" stroke-width="1.5" fill="none"/></svg></span></div>

<form class="abs search-bar">
  <div class="select" style="left:17px">Search by Practice</div>
  <div class="select" style="left:165px">Search by Lawyers name</div>
  <div class="select" style="left:313px">Search by Law firm name</div>
  <div class="select" style="left:461px">Search by Location</div>
  <div class="search-btn">Search</div>
</form>
<div class="abs search-shadow"></div>

<article class="card" style="left:71px">
  <div class="card-photo" role="img" aria-label="Visitors viewing framed calligraphy in a gallery" style="background:linear-gradient(90deg,#6b3b1e,#b39a74 40%,#8a5a2e 70%,#4a2a18)"></div>
  <h3>People Visiting</h3>
  <p>Dubai, the fast growing oil-exporting city located in the Arabian Gulf, has undergone a remarkable trans-formation. The United Arab Emirates</p>
  <a class="btn" href="#">More Info</a>
</article>
<article class="card" style="left:312px">
  <div class="card-photo" role="img" aria-label="Courtroom with judges seated at the bench" style="background:linear-gradient(180deg,#5a3a26,#8a6244 50%,#c9b4a0)"></div>
  <h3>Quality Law Firm</h3>
  <p style="margin-top:8px">Dubai, the fast growing oil-exporting city located in the Arabian Gulf, has undergone a remarkable trans-formation. The United Arab Emirates</p>
  <a class="btn" href="#">More Info</a>
</article>
<article class="card" style="left:552px">
  <div class="card-photo" role="img" aria-label="Two men working together in an office" style="background:linear-gradient(90deg,#dcdfe4,#c7ccd6 50%,#8e95a6)"></div>
  <h3>United Arab Emirates</h3>
  <p style="margin-top:8px">Dubai, the fast growing oil-exporting city located in the Arabian Gulf, has undergone a remarkable trans-formation. The United Arab Emirates</p>
  <a class="btn" href="#">More Info</a>
</article>

<h2 class="abs section-title" style="left:71px">Latest News</h2>
<div class="abs pager" style="left:411px">‹ ›</div>
<div class="abs rule" style="left:71px;width:366px"></div>

<div class="abs news-photo" style="top:850px;background:linear-gradient(90deg,#e6e1d8,#8d7a66 50%,#2e2a2a)" role="img" aria-label="Business leaders shaking hands at a signing event"></div>
<h3 class="abs news-title" style="top:846px;font-weight:400">Telvana and UAE Cedra Group Announce</h3>
<div class="abs news-date" style="top:870px">12-09-2013</div>
<p class="abs news-text" style="top:891px">Telvana, the leading global telecom player has signed a part-nership agreement with Dubai-based Cedra Group. This pact gives Telvana launchpad's startups <span class="read-more">Read More</span></p>
<div class="abs divider" style="top:959px"></div>

<div class="abs news-photo" style="top:985px;background:linear-gradient(90deg,#5a4a2a,#d8cfc0 45%,#3b3b3b)" role="img" aria-label="Men in traditional dress at a partnership ceremony"></div>
<h3 class="abs news-title" style="top:981px;font-weight:400">Cedra Group signs a regional partnership</h3>
<div class="abs news-date" style="top:1005px">12-09-2013</div>
<p class="abs news-text" style="top:1026px">In partnership with Cedra Group, Maison Linea, the London based bespoke luxury interior and architectural design firm will be headquartered in Dubai, <span class="read-more">Read More</span></p>

<h2 class="abs section-title" style="left:466px">Latest Blog</h2>
<div class="abs pager" style="left:752px">‹ ›</div>
<div class="abs rule" style="left:466px;width:312px"></div>

<article class="abs blog-card">
  <div class="blog-photo" role="img" aria-label="Wooden judge's gavel resting on a printed law book"></div>
  <h3>Working in the United Arab Emirates</h3>
  <hr>
  <div class="blog-meta">By sitewriters / In Blog, Medical, Text posts &nbsp;/ Comments(1)</div>
  <p>Dubai, the fast growing oil-exporting city located in the Arabian Gulf, has undergone a remarkable transformation. The United Arab Emirates (U.A.E.) through its leaders has implemented</p>
</article>

<footer class="site-footer">
  <div class="footer-links">Home | &nbsp;Find a Lawyer &nbsp;| &nbsp;Know your rights &nbsp;| &nbsp;About us &nbsp;| &nbsp;News &nbsp;| &nbsp;Articles &nbsp;| &nbsp;contact</div>
  <div class="copyright">© 2014. &nbsp;cedra group. All rights reserved. Terms of Use</div>
  <span class="social" style="left:623px"></span>
  <span class="social" style="left:655px"></span>
  <span class="social" style="left:687px"></span>
  <span class="social" style="left:720px"></span>
  <span class="social" style="left:752px"></span>
</footer>

</body>
</html>
```